Brochure Design Project

Gentle Willows is a family run all natural residential cleaning company
I am looking for 1 trifold brochure for all clients
I am looking for 2 holiday single sided brochure for deep cleanings and 20% off
(Holiday Ready? Or a Naughty list check list?)
I am looking for a single sided brochure to target specific buildings in SF ( I will change the building name to target). Limitations are that cleanings must be performed on Tuesday or Wednesday with cleaning arrival flexibility
1 single sided brochure for Office/Commercial Cleaning
Target Market(s)
Mom's, pet owners, people with disposable income
Industry/Entity Type
It Company
Font styles to use
Look and feel
Each slider illustrates characteristics of the customer's brand and the style your logo design should communicate.

```html
<!DOCTYPE html>
<html lang="en">
<head>
<meta charset="utf-8">
<title>Gentle Willows – Green Cleaning Flyer</title>
<link rel="stylesheet" href="https://fonts.googleapis.com/css2?family=Comfortaa:wght@400;600;700&family=Roboto:ital,wght@0,400;1,500&display=swap">
<style>
:root{
  --sky:#2aa9e0;
  --band:#17b0e4;
  --leaf:#6cc024;
  --mint:#f4fbec;
  --slate:#5f6166;
  --ink:#3d3d3d;
  --row:#eef4fa;
  --row-alt:#dde8f2;
  --row-text:#55606a;
  --white:#ffffff;
}
*{margin:0;padding:0;box-sizing:border-box}
html,body{width:854px;height:1200px;overflow:hidden;background:var(--white)}
.flyer{position:relative;width:854px;height:1200px;overflow:hidden;background:var(--mint);font-family:'Comfortaa',sans-serif}
.hero-photo{position:absolute;left:0;top:0;width:854px;height:580px;
  background:linear-gradient(180deg,#eef1f4 0%,#e2e7ec 45%,#c9b39a 62%,#b89c80 100%)}
.headline{position:absolute;right:48px;top:26px;text-align:right;color:var(--sky);white-space:nowrap;
  font-weight:700;font-size:41px;line-height:61px;text-shadow:0 0 6px #fff,0 0 2px #fff}
.inset{position:absolute;width:168px;height:168px;border-radius:50%;border:5px solid var(--white);
  box-shadow:0 2px 8px rgba(0,0,0,.25)}
.inset-lounge{left:606px;top:225px;background:linear-gradient(160deg,#dfe6ea,#c8cfd2 55%,#9ea4a3)}
.inset-kitchen{left:606px;top:405px;background:linear-gradient(160deg,#f2f2f0,#d9d6d0 55%,#8f8b84)}
.hero-edge{position:absolute;left:0;top:480px;width:854px;height:120px}
.rates{position:absolute;left:500px;top:500px;width:354px;height:560px}
.rates-bg{position:absolute;left:0;top:0;width:354px;height:150px}
.rates-fill{position:absolute;left:0;top:149px;width:354px;height:420px;background:var(--row)}
.rates-table{position:absolute;left:0;top:89px;width:354px;border-collapse:collapse;font-family:'Roboto',sans-serif}
.rates-table th{height:60px;color:var(--white);font-style:italic;font-weight:500;font-size:18px;vertical-align:middle;width:50%}
.rates-table td{height:46px;text-align:center;color:var(--row-text);font-size:14px;background:var(--row)}
.rates-table tr:nth-child(odd) td{background:var(--row-alt)}
.rates-table .contact-row td{text-align:left;padding-left:75px;background:var(--row)}
.intro{position:absolute;left:34px;top:596px;color:var(--sky);font-size:21px;line-height:33px;white-space:nowrap}
.body-copy{position:absolute;left:34px;top:718px;color:var(--ink);font-size:18px;line-height:32.5px;white-space:nowrap}
.offer{position:absolute;top:894px;width:126px;height:126px;border-radius:50%;color:var(--white);
  display:flex;flex-direction:column;align-items:center;justify-content:center;font-size:34px;line-height:36px}
.offer small{font-size:29px}
.offer-25{left:25px;background:var(--leaf)}
.offer-50{left:189px;background:var(--sky)}
.offer-90{left:341px;background:var(--slate)}
.brand{position:absolute;left:548px;top:1006px;display:flex;align-items:center;gap:10px;white-space:nowrap}
.brand-dot{width:40px;height:40px;border-radius:50%;background:var(--leaf)}
.brand-name{font-size:24px;font-weight:600;color:var(--slate);letter-spacing:1px}
.footer-band{position:absolute;left:0;top:1030px;width:854px;height:170px}
.tagline{position:absolute;left:91px;top:1080px;color:var(--white);font-size:28px;font-weight:600;white-space:nowrap}
.tagline small{font-size:23px}
.contact{position:absolute;display:flex;align-items:center;gap:8px;color:var(--white);font-size:19px;white-space:nowrap}
.contact-phone{left:34px;top:1143px}
.contact-mail{left:236px;top:1143px}
.contact-place{left:586px;top:1136px}
.icon{width:36px;height:36px;flex:none}
.address{font-size:16px;line-height:24px}
</style>
</head>
<body>
<main class="flyer">
  <div class="hero-photo" role="img" aria-label="Photo of a cleaner mopping a bright room beside a cleaning trolley and wet floor sign"></div>
  <h1 class="headline">San Francisco Bay's<br>premier green<br>cleaning service</h1>
  <div class="inset inset-lounge" role="img" aria-label="Photo of a clean living room with sofa by a window"></div>
  <div class="inset inset-kitchen" role="img" aria-label="Photo of a clean modern kitchen"></div>

  <svg class="hero-edge" viewBox="0 0 854 120" preserveAspectRatio="none" aria-hidden="true">
    <path d="M0 18 C200 95 420 95 854 40 L854 120 L0 120 Z" fill="var(--mint)"/>
    <path d="M0 18 C200 95 420 95 854 40" fill="none" stroke="var(--leaf)" stroke-width="8"/>
  </svg>

  <section class="rates">
    <svg class="rates-bg" viewBox="0 0 354 150" preserveAspectRatio="none" aria-hidden="true">
      <path d="M0 46 C120 40 240 30 354 20 L354 150 L0 150 Z" fill="var(--slate)"/>
      <path d="M0 46 C120 40 240 30 354 20" fill="none" stroke="var(--leaf)" stroke-width="6"/>
    </svg>
    <div class="rates-fill"></div>
    <table class="rates-table">
      <tr><th>Regular Cleaning</th><th>Deep Cleaning</th></tr>
      <tr><td>$100</td><td>$150</td></tr>
      <tr><td>$125</td><td>$250</td></tr>
      <tr><td>$150</td><td>$300</td></tr>
      <tr><td>$175 - $200</td><td>$350 - $400</td></tr>
      <tr><td>$225 - $275</td><td>$425 - $475</td></tr>
      <tr><td>$300 - $350</td><td>$500 - $550</td></tr>
      <tr class="contact-row"><td colspan="2">Contact Us</td></tr>
    </table>
  </section>

  <p class="intro">We deliver a greener, safer clean to<br>your home and your family with<br>our environmentally friendly products.</p>
  <p class="body-copy">We don’t cut corners with the use of harsh<br>chemicals and only use products that are<br>natural, environmentally friendly and safe<br>for your family and pets. It takes a little<br>more effort but we feel you’re worth it!</p>

  <div class="offer offer-25">25%<small>off</small></div>
  <div class="offer offer-50">50%<small>off</small></div>
  <div class="offer offer-90">90%<small>off</small></div>

  <div class="brand"><span class="brand-dot"></span><span class="brand-name">GENTLE WILLOWS</span></div>

  <svg class="footer-band" viewBox="0 0 854 170" preserveAspectRatio="none" aria-hidden="true">
    <path d="M0 34 C120 14 200 6 300 12 C420 20 500 58 600 56 C700 54 780 40 854 34 L854 170 L0 170 Z" fill="var(--band)"/>
  </svg>
  <p class="tagline">Live a Cleaner, <small>Greener Life</small></p>

  <span class="contact contact-phone">
    <svg class="icon" viewBox="0 0 36 36" aria-hidden="true"><circle cx="18" cy="18" r="16" fill="none" stroke="#fff" stroke-width="2"/><path d="M12 10c1-1 2-1 3 0l2 3c.5 1 0 2-1 2.5 1 2 2.5 3.5 4.5 4.5.5-1 1.5-1.5 2.5-1l3 2c1 1 1 2 0 3-2 2-5 1.5-9-2.5s-5-7-5-11.5z" fill="#fff"/></svg>
    (415) 555-0148
  </span>
  <span class="contact contact-mail">
    <svg class="icon" viewBox="0 0 36 36" aria-hidden="true"><circle cx="18" cy="18" r="16" fill="none" stroke="#fff" stroke-width="2"/><rect x="10" y="12" width="16" height="12" rx="1.5" fill="none" stroke="#fff" stroke-width="2"/><path d="M10 13l8 6 8-6" fill="none" stroke="#fff" stroke-width="2"/></svg>
    hello@gentlewillows.com
  </span>
  <span class="contact contact-place">
    <svg class="icon" viewBox="0 0 36 36" aria-hidden="true"><circle cx="18" cy="18" r="16" fill="none" stroke="#fff" stroke-width="2"/><path d="M18 27s-6-6.5-6-11a6 6 0 0 1 12 0c0 4.5-6 11-6 11z" fill="none" stroke="#fff" stroke-width="2"/><circle cx="18" cy="16" r="2" fill="#fff"/></svg>
    <span class="address">92 Alder Lane, 3rd floor<br>San Francisco CA 94110</span>
  </span>
</main>
</body>
</html>
```